A simple Chatterbook Ad (not Chatterbook Page) for weight loss surgery

It’s a simple ad in terms of the text.

The text should say:
Curious about weight loss surgery?
This 30 second quiz will tell you which procedure will suit you best

I'm open to variations in the text if it is thought to enhance the ad.

Targeted towards obese individuals who have been unable to lose weight with diet and exercise. My industry is weight loss surgery – webpage www.marcusbellweather.com.au. Clicking the ad leads to a quiz on my webpage relating to weight loss surgery. Most frequent users of this service are females (75%) between ages of 35 and 55 years.

Successful weight loss surgery can enable individuals who have been unable to lose weight to lose a substantial amount of the excess weight they are carrying to be healthier and happier.

```html
<!DOCTYPE html>
<html lang="en">
<head>
<meta charset="utf-8">
<title>Marcus Bellweather – Weight Loss Surgery Ad</title>
<link href="https://fonts.googleapis.com/css2?family=Bebas+Neue&family=Poppins:wght@400;500;700;800&display=swap" rel="stylesheet">
<style>
  :root {
    --teal: #16938a;
    --ink: #1d1d1d;
    --white: #ffffff;
    --silver-1: #f4f4f4;
    --silver-2: #b9b9b9;
    --grey-text: #6f6f6f;
    --scale-dark: #3a3d3f;
    --scale-mid: #7d8286;
  }
  * { margin: 0; padding: 0; box-sizing: border-box; }
  html, body { width: 1200px; height: 1200px; overflow: hidden; background: var(--white); }
  .ad {
    position: relative;
    width: 1200px;
    height: 1200px;
    overflow: hidden;
    background: var(--white);
    font-family: "Poppins", sans-serif;
    color: var(--ink);
  }
  .brand {
    position: absolute;
    left: 64px;
    top: 70px;
    display: flex;
    align-items: center;
    gap: 14px;
  }
  .brand-dot {
    width: 62px; height: 62px;
    border-radius: 50%;
    background: var(--teal);
  }
  .brand-name {
    font-size: 30px;
    font-weight: 700;
    color: var(--teal);
    line-height: 1;
    letter-spacing: 0.5px;
  }
  .brand-role {
    font-size: 11px;
    font-weight: 500;
    color: var(--grey-text);
    letter-spacing: 1.6px;
    text-transform: uppercase;
    margin-top: 6px;
  }
  .headline-lead {
    position: absolute;
    left: 62px;
    top: 194px;
    font-size: 64px;
    font-weight: 800;
    line-height: 1;
    letter-spacing: 1.2px;
  }
  .headline-main {
    position: absolute;
    left: 60px;
    top: 270px;
    font-family: "Bebas Neue", sans-serif;
    font-weight: 400;
    color: var(--teal);
    line-height: 0.82;
  }
  .headline-main .line-1 {
    display: block;
    font-size: 158px;
    letter-spacing: 0;
    transform: scaleX(0.93);
    transform-origin: left center;
  }
  .headline-main .line-2 { display: block; font-size: 199px; letter-spacing: 1px; margin-top: -8px; }
  .subline {
    position: absolute;
    left: 64px;
    top: 556px;
    width: 575px;
    font-size: 40px;
    font-weight: 700;
    line-height: 50px;
  }
  .rule {
    position: absolute;
    left: 0; top: 739px;
    width: 620px; height: 14px;
    background: var(--teal);
  }
  .info-band {
    position: absolute;
    left: 0; top: 753px;
    width: 630px; height: 182px;
    background: linear-gradient(180deg, var(--silver-2) 0%, var(--silver-1) 30%, var(--white) 55%, var(--silver-1) 78%, var(--silver-2) 100%);
  }
  .info-band p {
    position: absolute;
    left: 64px; top: 22px;
    width: 535px;
    font-size: 20.5px;
    line-height: 27px;
    font-weight: 400;
    color: #2a2a2a;
  }
  .contact-band {
    position: absolute;
    left: 0; top: 934px;
    width: 1200px; height: 266px;
    background: var(--teal);
  }
  .photo-frame {
    position: absolute;
    left: 0; top: 0;
    width: 1200px; height: 1200px;
  }
  .scale-photo {
    position: absolute;
    left: 730px; top: 0;
    width: 390px; height: 386px;
    border-radius: 0 0 60px 60px;
    border: 4px solid var(--teal);
    outline: 8px solid var(--white);
    background: linear-gradient(160deg, var(--scale-mid) 0%, var(--scale-dark) 100%);
  }
  .contact {
    position: absolute;
    left: 68px;
    top: 972px;
    color: var(--white);
  }
  .contact-lead { font-size: 27px; font-weight: 400; letter-spacing: 0.3px; line-height: 1; }
  .contact-lead strong { font-weight: 700; }
  .contact-row { display: flex; align-items: center; gap: 16px; }
  .contact-phone { margin-top: 24px; font-size: 62px; font-weight: 700; line-height: 1; }
  .contact-web { margin-top: 16px; font-size: 33px; font-weight: 700; line-height: 1; }
  .icon { flex: none; }
</style>
</head>
<body>
<div class="ad">
  <div class="contact-band"></div>

  <svg class="photo-frame" viewBox="0 0 1200 1200" aria-hidden="true">
    <defs>
      <linearGradient id="ringSilver" x1="0" y1="0" x2="1" y2="1">
        <stop offset="0" stop-color="#ffffff"/>
        <stop offset="0.5" stop-color="#c8c8c8"/>
        <stop offset="1" stop-color="#f2f2f2"/>
      </linearGradient>
      <linearGradient id="photoTone" x1="0" y1="0" x2="1" y2="1">
        <stop offset="0" stop-color="#8a6b55"/>
        <stop offset="0.45" stop-color="#d9c3b3"/>
        <stop offset="1" stop-color="#ecebea"/>
      </linearGradient>
    </defs>
    <circle cx="1065" cy="806" r="455" fill="var(--teal)"/>
    <circle cx="1065" cy="806" r="438" fill="url(#ringSilver)"/>
  </svg>

  <svg class="photo-frame" viewBox="0 0 1200 1200" role="img" aria-label="Photo: a smiling woman in black sportswear having her waist measured with a tape by a female doctor in a white coat">
    <circle cx="1065" cy="806" r="420" fill="url(#photoTone)"/>
  </svg>

  <div class="rule"></div>
  <div class="info-band">
    <p>Successful weight loss surgery can enable individuals who have been unable to lose weight to lose a substantial amount of the excess weight they are carrying to be healthier and happier.</p>
  </div>

  <div class="scale-photo" role="img" aria-label="Photo: bare feet standing on a bathroom scale"></div>

  <div class="brand">
    <span class="brand-dot"></span>
    <div>
      <div class="brand-name">MARCUS BELLWEATHER</div>
      <div class="brand-role">General, Upper GI &amp; Bariatric Surgeon</div>
    </div>
  </div>

  <h1 class="headline-lead">CURIOUS ABOUT</h1>
  <h2 class="headline-main">
    <span class="line-1">WEIGHT LOSS</span>
    <span class="line-2">SURGERY?</span>
  </h2>
  <p class="subline">This 30 second quiz will tell you which procedure will suit you best</p>

  <div class="contact">
    <p class="contact-lead">CONTACT US FOR <strong>ALL APPOINTMENTS</strong></p>
    <p class="contact-row contact-phone">
      <svg class="icon" width="44" height="44" viewBox="0 0 24 24" aria-hidden="true">
        <path fill="#fff" d="M6.6 10.8a15.1 15.1 0 0 0 6.6 6.6l2.2-2.2c.3-.3.7-.4 1-.2 1.1.4 2.3.6 3.6.6.6 0 1 .4 1 1V20c0 .6-.4 1-1 1A17 17 0 0 1 3 4c0-.6.4-1 1-1h3.5c.6 0 1 .4 1 1 0 1.3.2 2.5.6 3.6.1.3 0 .7-.2 1z"/>
        <path fill="none" stroke="#fff" stroke-width="1.6" stroke-linecap="round" d="M14.5 6.5a3.5 3.5 0 0 1 3 3M14.5 3a7 7 0 0 1 6.5 6.5"/>
      </svg>
      03 9000 4127
    </p>
    <p class="contact-row contact-web">
      <svg class="icon" width="38" height="38" viewBox="0 0 24 24" aria-hidden="true">
        <g fill="none" stroke="#fff" stroke-width="1.8">
          <circle cx="12" cy="12" r="10"/>
          <ellipse cx="12" cy="12" rx="4.5" ry="10"/>
          <path d="M2 12h20M4 6.5h16M4 17.5h16"/>
        </g>
      </svg>
      www.marcusbellweather.com.au
    </p>
  </div>
</div>
</body>
</html>
```